Marta Belle Designs & Events business card

I need an elegant informative but not busy business card using my logo. We are a florist with high end customers. I am adding a PDF file and a PNG file for those who requested it
Updates

Target Market(s)

Brides, grooms, men purchasing flowers
Ages 20-65

Industry/Entity Type

Florist

Requirements
Must have
• Business info:
Marta Belle Design & Events
www.martabelleevents-sample.com.
555-418-2763

555-418-2763
Nice to have
• Est 1954
may want Pinterest logo, twitter and linkedin and facbook
Should not have
• Clip art or photos

```html
<!DOCTYPE html>
<html lang="en">
<head>
<meta charset="utf-8">
<title>Marta Belle Designs &amp; Events – Business Card</title>
<link rel="stylesheet" href="https://fonts.googleapis.com/css2?family=Cinzel:wght@400&family=Cormorant+Garamond:wght@400;500&display=swap">
<style>
  :root {
    --paper: #ffffff;
    --ink: #1a1a1a;
    --blush: #f2aeb8;
    --edge: #3a3a3a;
  }
  * { margin: 0; padding: 0; box-sizing: border-box; }
  html, body {
    width: 1200px;
    height: 619px;
    overflow: hidden;
    background: var(--paper);
  }
  .canvas {
    position: relative;
    width: 1200px;
    height: 619px;
  }
  .card {
    position: absolute;
    top: 147px;
    width: 557px;
    height: 350px;
    border: 1.5px solid var(--edge);
    background: var(--paper);
  }
  .card--front { left: 27px; }
  .card--back  { left: 610px; }

  .brand-mark {
    position: absolute;
    left: 50%;
    transform: translateX(-50%);
    display: block;
  }
  .card--front .brand-mark { top: 88px; }
  .card--back  .brand-mark { top: 54px; }

  .brand-name {
    position: absolute;
    left: 0;
    right: 0;
    text-align: center;
    font-family: "Cinzel", serif;
    font-weight: 400;
    color: var(--ink);
  }
  .brand-name__main {
    top: 193px;
    font-size: 37px;
    letter-spacing: 6px;
  }
  .brand-name__sub {
    top: 247px;
    font-size: 11px;
    letter-spacing: 3.5px;
  }

  .established {
    position: absolute;
    top: 206px;
    left: 0;
    right: 0;
    text-align: center;
    font-family: "Cormorant Garamond", serif;
    font-size: 11px;
    color: var(--ink);
  }

  .contact-line {
    position: absolute;
    top: 303px;
    left: 0;
    right: 0;
    text-align: center;
    font-family: "Cormorant Garamond", serif;
    font-size: 14.5px;
    white-space: nowrap;
  }
  .contact-line__company,
  .contact-line__phone { color: var(--blush); }
  .contact-line__web { color: var(--ink); margin: 0 6px; }
</style>
</head>
<body>
<main class="canvas">

  <section class="card card--front" aria-label="Card front">
    <svg class="brand-mark" width="92" height="92" viewBox="0 0 92 92" aria-hidden="true">
      <circle cx="46" cy="46" r="43" fill="none" stroke="var(--blush)" stroke-width="2"/>
    </svg>
    <p class="brand-name brand-name__main">MARTA BELLE</p>
    <p class="brand-name brand-name__sub">DESIGNS &amp; EVENTS</p>
  </section>

  <section class="card card--back" aria-label="Card back">
    <svg class="brand-mark" width="140" height="140" viewBox="0 0 140 140" aria-hidden="true">
      <circle cx="70" cy="70" r="66" fill="none" stroke="var(--blush)" stroke-width="2.5"/>
    </svg>
    <p class="established">Est 1954</p>
    <p class="contact-line">
      <span class="contact-line__company">Marta Belle Design &amp; Events</span>
      <span class="contact-line__web">www.martabelleevents-sample.com.</span>
      <span class="contact-line__phone">555-418-2763</span>
    </p>
  </section>

</main>
</body>
</html>
```